Meridian Rest Supply Needs Business Card

Looking for a very nice looking business card. Creative but not extravagant. We sell beds and pillows across the U.S. and need something professional but catchy. I have attached the logo.

Name : Dale Fenwick
Title : President
Phone : (800) 417-2964
Email: sleep@quorvana.com
Website: www.quorvana.com

Can be single-sided or double-sided
horizontal or vertical

Can use Blues/Greys

Target Market(s)

Mass Market

Industry/Entity Type

Retail

Contact Information for Business Card

Name : Dale Fenwick
Title : President
Phone : (800) 417-2964
Email: sleep@quorvana.com
Website: www.quorvana.com

Requirements
Must have
• Clean, Modern, Smooth
• Can use Blues/Greys
• On the other side without the information - have something simple like www.quorvana.com or our logo
Nice to have
• Surprise me
Should not have
• Nothing crazy, nothing cluttered

```html
<!DOCTYPE html>
<html lang="en">
<head>
<meta charset="utf-8">
<title>Meridian Rest Supply – Business Card</title>
<link rel="stylesheet" href="https://fonts.googleapis.com/css2?family=Roboto:wght@300;400;700&display=swap">
<style>
  :root {
    --backdrop: #e6e8eb;
    --brand-blue: #36a9de;
    --brand-blue-deep: #1f8fc6;
    --brand-blue-light: #5cc0ec;
    --ink: #3d3f42;
    --slate: #55595e;
    --paper: #ffffff;
    --paper-shade: #eceef0;
  }
  * { box-sizing: border-box; margin: 0; padding: 0; }
  html, body { width: 1200px; height: 843px; overflow: hidden; }
  body {
    background: var(--backdrop);
    font-family: "Roboto", Arial, sans-serif;
    display: flex;
    align-items: center;
    justify-content: center;
    gap: 40px;
  }
  .card {
    position: relative;
    width: 540px;
    height: 309px;
    overflow: hidden;
    box-shadow: 0 10px 28px rgba(0,0,0,0.18);
  }

  /* Back side */
  .card-back {
    background: linear-gradient(160deg, var(--brand-blue-light) 0%, var(--brand-blue) 45%, var(--brand-blue-deep) 100%);
    display: flex;
    flex-direction: column;
    align-items: center;
    justify-content: center;
    color: var(--paper);
  }
  .card-back .wordmark {
    font-size: 74px;
    font-weight: 300;
    letter-spacing: 1px;
    line-height: 1;
    color: var(--paper);
  }
  .card-back .web {
    margin-top: 18px;
    font-size: 10px;
    letter-spacing: 6px;
    color: rgba(255,255,255,0.85);
  }

  /* Front side */
  .card-front {
    background: linear-gradient(150deg, var(--paper) 40%, var(--paper-shade) 100%);
  }
  .card-front .wordmark {
    position: absolute;
    right: 28px;
    top: 74px;
    font-size: 60px;
    font-weight: 300;
    line-height: 1;
    color: var(--brand-blue);
  }
  .name-band {
    position: absolute;
    left: 0;
    top: 110px;
    width: 290px;
    height: 44px;
  }
  .rule {
    position: absolute;
    left: 262px;
    right: 0;
    top: 152px;
    height: 3px;
    border-top: 1px solid var(--brand-blue);
    border-bottom: 1px solid rgba(54,169,222,0.45);
  }
  .identity {
    position: absolute;
    left: 28px;
    top: 114px;
    color: var(--paper);
  }
  .identity .person { font-size: 15px; font-weight: 700; line-height: 18px; }
  .identity .role { font-size: 12px; font-weight: 400; line-height: 15px; }
  .contacts {
    position: absolute;
    left: 28px;
    top: 168px;
    list-style: none;
    font-size: 12.5px;
    color: var(--ink);
  }
  .contacts li {
    display: flex;
    align-items: center;
    gap: 8px;
    height: 19px;
  }
  .contacts svg { width: 12px; height: 12px; flex: none; }
</style>
</head>
<body>

  <section class="card card-back" aria-label="Card back">
    <div class="wordmark">quorvana</div>
    <div class="web">www.quorvana.com</div>
  </section>

  <section class="card card-front" aria-label="Card front">
    <div class="wordmark">quorvana</div>

    <svg class="name-band" viewBox="0 0 290 44" aria-hidden="true">
      <polygon points="0,0 250,0 222,44 0,44" fill="var(--brand-blue)"/>
      <polygon points="256,0 264,0 236,44 228,44" fill="var(--slate)"/>
    </svg>
    <div class="rule"></div>

    <div class="identity">
      <div class="person">Dale Fenwick</div>
      <div class="role">President</div>
    </div>

    <ul class="contacts">
      <li>
        <svg viewBox="0 0 12 12" aria-hidden="true">
          <path d="M3 1 L5 3.5 L4 5 Q5 7 7 8 L8.5 7 L11 9 L9.5 11 Q2 10 1 2.5 Z" fill="var(--brand-blue)"/>
        </svg>
        (800) 417-2964
      </li>
      <li>
        <svg viewBox="0 0 12 12" aria-hidden="true">
          <rect x="0.5" y="2.5" width="11" height="7.5" rx="1" fill="var(--brand-blue)"/>
          <polyline points="1,3.2 6,7 11,3.2" fill="none" stroke="#fff" stroke-width="1"/>
        </svg>
        sleep@quorvana.com
      </li>
      <li>
        <svg viewBox="0 0 12 12" aria-hidden="true">
          <circle cx="6" cy="6" r="5.5" fill="var(--brand-blue)"/>
          <ellipse cx="6" cy="6" rx="2.2" ry="5" fill="none" stroke="#fff" stroke-width="0.8"/>
          <line x1="1" y1="6" x2="11" y2="6" stroke="#fff" stroke-width="0.8"/>
        </svg>
        www.quorvana.com
      </li>
    </ul>
  </section>

</body>
</html>
```